Website Design for Satellite Data/HighTech Company

Please read the full description of what we want here:
https://files.brivantodocs.net/sheet/d/7QpwLx3Kv-Tn9eRbuM2fHc0JsYd4aWkZ8oNe-q5tVrBu/view?mode=share
We want a nice landing page/static website for the company. Modern and attractive, visually oriented with illustrations where pertinent. It should be static, in other words not based on wordpress or any other system, just HTML files using CSS and javascript. We should be able to just open it from the disk in our laptop with a browser and see it.
Target Market(s)
AgriTech
Industry/Entity Type
AgriTech
Coding
Coded - Design and coding required
Number of Pages Required
3 page
Look and feel
Each slider illustrates characteristics of the customer's brand and the style your logo design should communicate.

```html
<!DOCTYPE html>
<html lang="en">
<head>
<meta charset="utf-8">
<title>Orbiqa — Satellite Monitoring for Agriculture</title>
<link href="https://fonts.googleapis.com/css2?family=Baloo+2:wght@700&family=Exo+2:wght@500;600&family=Poppins:wght@400;500;600&display=swap" rel="stylesheet">
<style>
:root{
  --orange:#ea5a0c;
  --footer:#ec7a3c;
  --ink:#2b2d33;
  --grey:#7a7d84;
  --soft:#f5f7fa;
  --panel:#242422;
  --navy:#1f2b5e;
  --white:#ffffff;
}
*{margin:0;padding:0;box-sizing:border-box}
html,body{width:1200px;height:1200px;overflow:hidden;background:var(--white)}
.stage{position:absolute;left:0;top:0;width:1932px;height:1932px;transform:scale(0.62112);transform-origin:0 0;font-family:"Poppins",sans-serif;color:var(--ink)}
.page{position:absolute;left:540px;top:0;width:851px;height:1932px;overflow:hidden}
.abs{position:absolute}
.center{text-align:center}

/* hero */
.hero{top:0;left:0;width:851px;height:385px}
.hero-photo{position:absolute;inset:0;background:linear-gradient(100deg,#2f6e1c 0%,#4f9b2c 35%,#6fb53c 60%,#3f8a24 100%)}
.logo{left:25px;top:28px;color:var(--white);font-family:"Exo 2",sans-serif;font-weight:600;font-size:24px;letter-spacing:3px;display:flex;align-items:center;gap:6px}
.logo .dot{width:16px;height:16px;border:2px solid var(--white);border-radius:50%}
.nav{top:18px;left:0;width:851px;font-size:7.5px;font-weight:600;color:var(--white)}
.nav span{position:absolute;top:2px}
.nav .active::after{content:"";position:absolute;left:-10px;right:-10px;top:16px;height:2px;background:var(--white)}
.nav-cta{position:absolute;left:704px;top:-4px;width:68px;height:21px;border-radius:11px;background:var(--orange);font-size:7.5px;display:flex;align-items:center;justify-content:center}
.hero h1{left:58px;top:120px;font-family:"Baloo 2",sans-serif;font-size:44px;line-height:54px;color:var(--white);font-weight:700}
.hero .tag{left:60px;top:235px;font-size:11px;color:var(--white)}
.btn{position:absolute;height:32px;border-radius:16px;font-size:9px;font-weight:600;display:flex;align-items:center;justify-content:center;color:var(--white)}
.btn-solid{background:var(--orange)}
.btn-line{border:1px solid var(--white);font-weight:500}

/* capabilities */
.caps{top:385px;left:0;width:851px;height:365px;background:var(--soft)}
.eyebrow{font-family:"Exo 2",sans-serif;font-weight:500;font-size:20px;color:var(--orange);width:100%}
.heading{font-family:"Exo 2",sans-serif;font-weight:500;font-size:29px;width:100%}
.sub{font-size:9.5px;color:var(--grey);width:100%;line-height:14px}
.card{top:142px;width:241px;height:173px;background:var(--white);box-shadow:0 2px 8px rgba(0,0,0,.07);text-align:center}
.card .icon{width:48px;height:48px;margin:12px auto 0;border-radius:10px;background:linear-gradient(135deg,#9fc8f2,#f2b66a)}
.card h3{font-size:11px;font-weight:500;margin-top:14px}
.card p{font-size:9px;line-height:14px;color:#4a4c52;margin:15px 22px 0}

/* expertise */
.expertise{top:750px;left:0;width:851px;height:580px}
.exp-photo{position:absolute;inset:0;background:linear-gradient(180deg,#45474a 0%,#3a3c3d 60%,#3a3830 100%)}
.expertise .heading{color:var(--white)}
.exp-text{left:36px;width:779px;top:113px;color:#e8e8e8;font-size:9.5px;line-height:14.3px;text-align:center}
.exp-text p{margin-bottom:14.3px}
.ethos{left:28px;top:290px;width:791px;height:190px;background:var(--panel);border:1px solid #5a5a58;color:var(--white)}
.ethos h3{font-weight:400;font-size:18.5px;text-align:center;margin-top:17px}
.ethos .intro{font-size:9.5px;line-height:14.3px;text-align:center;margin:12px 20px 0;color:#e6e6e6}
.ethos-item{top:108px;display:flex;gap:11px;align-items:center;font-size:9.5px;line-height:14.3px;color:#ececec}
.learn{left:350px;top:508px;width:171px;height:28px;border:1px solid #d8d8d8;border-radius:14px;color:var(--white);font-size:9px;display:flex;align-items:center;justify-content:center}

/* customers */
.customers{top:1330px;left:0;width:851px;height:440px;background:var(--white)}
.client{top:160px;width:240px;text-align:center}
.client .name{font-weight:600;font-size:26px;color:var(--navy);height:52px;display:flex;align-items:center;justify-content:center;gap:8px}
.client .name.small{font-size:12px;color:#3a3a3a;text-align:left;line-height:15px}
.client .name.light{font-weight:400;color:#555}
.client .mark{width:30px;height:30px;background:#3a3a5a;flex:none}
.client p{font-size:9.5px;line-height:14.3px;color:#3a3c42;margin-top:15px}
.partners{top:368px;left:40px;width:760px;display:flex;justify-content:space-between;align-items:center}
.partners span{font-size:13px;font-weight:600;color:#3c4a7a}

/* footer */
.footer{top:1770px;left:0;width:851px;height:162px;background:var(--footer);color:var(--white)}
.f-col{top:22px;width:250px;text-align:center;font-size:9.5px;line-height:14.3px}
.f-col strong{display:block;margin-top:8px;font-weight:600}
.f-btn{left:328px;top:113px;width:171px;height:28px;border:1px solid var(--white);border-radius:14px;font-size:9px;display:flex;align-items:center;justify-content:center}
</style>
</head>
<body>
<div class="stage">
<div class="page">

  <section class="hero abs">
    <div class="hero-photo" role="img" aria-label="Close-up photo of a green wheat field"></div>
    <div class="logo abs"><span>ORBIQA</span><span class="dot"></span></div>
    <nav class="nav abs">
      <span style="left:260px">ES</span>
      <span class="active" style="left:368px">HOME</span>
      <span style="left:418px">ABOUT</span>
      <span style="left:471px">PRODUCTS</span>
      <span style="left:540px">TECHNOLOGIES</span>
      <span style="left:626px">WORK ETHOS</span>
      <div class="nav-cta">CONTACT US</div>
    </nav>
    <h1 class="abs">Satellite Monitoring<br>For Agriculture</h1>
    <div class="tag abs">FOR GOVERNMENTS, BUSINESS, INDUSTRY AND RESEARCH</div>
    <div class="btn btn-solid" style="left:56px;top:279px;width:101px">GET STARTED</div>
    <div class="btn btn-line" style="left:170px;top:279px;width:100px">DEMO</div>
  </section>

  <section class="caps abs">
    <div class="eyebrow abs center" style="top:36px">OUR CAPABILITIES</div>
    <div class="heading abs center" style="top:62px">HIGH END SOFTWARE ENGINEERING</div>
    <div class="sub abs center" style="top:104px">Built by expert software engineers, mathematicians, industry and field experts.</div>
    <div class="card abs" style="left:28px">
      <div class="icon" role="img" aria-label="Data science illustration"></div>
      <h3>Data Science &amp; Artificial Intelligence</h3>
      <p>Orbiqa provides you with the necessary support to develop your highly complex engineering products for your business.</p>
    </div>
    <div class="card abs" style="left:303px">
      <div class="icon" role="img" aria-label="Cloud computing illustration"></div>
      <h3>Cloud Computing</h3>
      <p>Orbiqa provides you with the necessary support to develop your highly complex engineering products for your business.</p>
    </div>
    <div class="card abs" style="left:578px">
      <div class="icon" role="img" aria-label="Software architecture illustration"></div>
      <h3>Software Systems Architecture</h3>
      <p>Orbiqa provides you with the necessary support to develop your highly complex engineering products for your business.</p>
    </div>
  </section>

  <section class="expertise abs">
    <div class="exp-photo" role="img" aria-label="Dimmed photo of satellite dish antennas"></div>
    <div class="eyebrow abs center" style="top:30px;padding-left:40px">OUR EXPERTISE</div>
    <div class="heading abs center" style="top:56px;padding-left:30px">WELCOME TO ORBIQA</div>
    <div class="exp-text abs">
      <p>Orbiqa B.V. is a company based in The Netherlands that provides specialized software for two important industries: Earth Observation technologies and High Tech Systems.</p>
      <p>Orbiqa provides you with the necessary support to develop your highly complex engineering products for your business. Our consulting services and our capacities provide you with the certainty that your efforts in engineering and R&amp;D will align with your objectives. We have a solid base in technical knowledge complemented with 20+ years of experience.</p>
      <p>We have developed products for academic and research institutions as well as commercial companies in the USA, Europe and Latin America. From medium sized business to large corporations, in local or regional contexts, we deliver your project in compliance with technical requirements, objectives and time frames.</p>
    </div>
    <div class="ethos abs">
      <h3>Work Ethos</h3>
      <p class="intro">Organization and order are important factors for the delivery of successful projects and the creation of high impact products. Motivation and a good working environment are key. Our work ethos involves:</p>
      <div class="ethos-item abs" style="left:24px">
        <svg width="25" height="25" viewBox="0 0 25 25"><circle cx="12.5" cy="12.5" r="11" fill="none" stroke="#fff" stroke-width="1.2"/><path d="M7 12.5l4 4 8-9" fill="none" stroke="#fff" stroke-width="1.2"/></svg>
        <span>Refining requirements and<br>communications with all involved parties</span>
      </div>
      <div class="ethos-item abs" style="left:287px">
        <svg width="25" height="25" viewBox="0 0 25 25"><circle cx="12.5" cy="12.5" r="11" fill="none" stroke="#fff" stroke-width="1.2"/><path d="M7 12.5l4 4 8-9" fill="none" stroke="#fff" stroke-width="1.2"/></svg>
        <span>Plan and organize work packages to meet<br>these requirements</span>
      </div>
      <div class="ethos-item abs" style="left:555px">
        <svg width="25" height="25" viewBox="0 0 25 25"><circle cx="12.5" cy="12.5" r="11" fill="none" stroke="#fff" stroke-width="1.2"/><path d="M7 12.5l4 4 8-9" fill="none" stroke="#fff" stroke-width="1.2"/></svg>
        <span>Plan follow up meetings to report and<br>discuss status</span>
      </div>
    </div>
    <div class="learn abs">Learn More</div>
  </section>

  <section class="customers abs">
    <div class="eyebrow abs center" style="top:34px;padding-left:20px">USE CASES</div>
    <div class="heading abs center" style="top:60px;padding-left:20px">OUR CUSTOMERS</div>
    <div class="sub abs center" style="top:102px;padding:0 100px">We feel proud to be able to provide information and high quality services to our customers in Europe and Latin America. Our services give them a competitive advantage over their competitors.</div>
    <div class="client abs" style="left:30px">
      <div class="name">AERVINTO</div>
      <p>Aervinto required the development of analytic platforms for their scientists and engineers to work with Earth Observation data, focusing on air quality. We developed a cloud-based environment that is able to manipulate and visualize data in one single interface.</p>
    </div>
    <div class="client abs" style="left:291px">
      <div class="name small"><span class="mark"></span><span>MINISTERIO DE<br>TIERRAS Y AGUAS</span></div>
      <p>Regional government agency responsible for policy, management and monitoring of natural resources and the environment. We have provided them with maps and data to evaluate the impact and effects of natural disasters and urban development.</p>
    </div>
    <div class="client abs" style="left:572px">
      <div class="name light">quenlo</div>
      <p>Quenlo Trading Group LLC is a company based in the USA dedicated to the logistics and export of commodities such as quinoa, chia, sesame, nuts and other agricultural products from South America to the world. Our periodic data provides them the location and quantification of growth fields of these products so they can properly plan their operations.</p>
    </div>
    <div class="partners abs">
      <span>Grupo Ondara</span>
      <span>Pellacor Capital</span>
      <span>Tavrin Tech</span>
      <span>Astrelle</span>
      <span>Banco Velmara</span>
      <span>Ruta Dinámica</span>
    </div>
  </section>

  <footer class="footer abs">
    <div class="f-col abs" style="left:26px">
      <svg width="20" height="26" viewBox="0 0 20 26"><path d="M10 24s8-8.5 8-14a8 8 0 0 0-16 0c0 5.5 8 14 8 14z" fill="none" stroke="#fff" stroke-width="1.6"/><circle cx="10" cy="10" r="3" fill="none" stroke="#fff" stroke-width="1.6"/></svg>
      <strong>Address:</strong>Keizerskade 12, 2511 KR, The<br>Hague, The Netherlands
    </div>
    <div class="f-col abs" style="left:288px">
      <svg width="26" height="26" viewBox="0 0 26 26"><circle cx="13" cy="13" r="4.5" fill="none" stroke="#fff" stroke-width="1.8"/><path d="M17.5 9v5.5a3 3 0 0 0 6 0V13a10.5 10.5 0 1 0-4 8.2" fill="none" stroke="#fff" stroke-width="1.8"/></svg>
      <strong>Email:</strong>info@orbiqa.nl
    </div>
    <div class="f-col abs" style="left:577px">
      <svg width="20" height="26" viewBox="0 0 20 26"><path d="M10 24s8-8.5 8-14a8 8 0 0 0-16 0c0 5.5 8 14 8 14z" fill="none" stroke="#fff" stroke-width="1.6"/><rect x="7" y="6" width="6" height="8" fill="none" stroke="#fff" stroke-width="1.4"/></svg>
      <strong>Company Info:</strong>Chamber of Commerce (KvK): 71042958<br>Tax Number (BTW): NL804517226B01
    </div>
    <div class="f-btn abs">CONTACT US</div>
  </footer>

</div>
</div>
</body>
</html>
```